mobile app maker needs website redone

We currently have a running website that generates some traffic and looks ok but now we want to revamp it with professional modern eye catching design.
We are open to proposals and open to any new ideas or suggestions but we have to see your previous work.
our current site is www.brivelapp.com

Industry/Entity Type

It Professional

Coding

Coded - Design and coding required

Number of Pages Required

5+ page

Font styles to use
Serif
Other font styles liked:
• open

Requirements
Must have
• modern look and feel easy to use
Nice to have
• responsive websites , example are as follow ,http://quonpage-template.sitemorra.io , dalvo.com , http://marpex.sitemorra.io

```html
<!DOCTYPE html>
<html lang="en">
<head>
<meta charset="utf-8">
<title>Brivel Marketing — Mobile Apps &amp; Mobile Websites</title>
<link href="https://fonts.googleapis.com/css2?family=Oswald:wght@400;500&family=Ubuntu:wght@400;500&family=Roboto:wght@400;500;700&display=swap" rel="stylesheet">
<style>
:root{
  --hero-blue:#1f5f9e;
  --hero-deep:#173f73;
  --brand-blue:#1d82cf;
  --icon-blue:#2a8be0;
  --green:#3aa04a;
  --green-dark:#2f8a3d;
  --nav-active:#5fd16b;
  --ink:#333;
  --muted:#666;
  --pale-blue:#dcebf8;
  --footer-blue:#1d6db5;
  --black:#1a1a1a;
  --white:#fff;
}
*{box-sizing:border-box;margin:0;padding:0}
html,body{width:1200px;height:3495px;overflow:hidden}
body{font-family:'Roboto',sans-serif;color:var(--ink);position:relative;background:var(--white)}
section,header,footer{position:absolute;left:0;width:1200px}
.abs{position:absolute}

/* Hero */
.hero{top:0;height:710px;background:linear-gradient(135deg,#2668a8 0%,var(--hero-blue) 45%,var(--hero-deep) 100%)}
.brand{left:92px;top:22px;width:170px;text-align:center;color:var(--white);font-family:'Ubuntu',sans-serif;font-weight:500;font-size:21px}
.brand-mark{display:block;width:34px;height:34px;margin:0 auto 8px;background:var(--white);border-radius:50%}
.nav{left:394px;top:76px;display:flex;gap:24px;font-size:13px;color:var(--white);text-transform:uppercase}
.nav .active{color:var(--nav-active)}
.btn-login{left:1042px;top:67px;border:1px solid var(--white);color:var(--white);font-size:12px;padding:7px 13px;border-radius:3px}
.hero-title{left:92px;top:270px;font-family:'Ubuntu',sans-serif;color:var(--white)}
.hero-title h1{font-size:33px;font-weight:500;letter-spacing:.5px}
.hero-title h2{font-size:26px;font-weight:400;margin-top:2px}
.hero-title p{font-size:16px;line-height:24px;margin-top:14px;width:520px}
.btn{display:inline-block;color:var(--white);font-size:18px;padding:14px 22px;border-radius:3px}
.btn-green{background:linear-gradient(#49b553,var(--green-dark))}
.btn-blue{background:linear-gradient(#3b9ee8,#1f78c8)}
.hero .btn{position:absolute;left:88px;top:442px}
.slider-arrows{left:92px;top:636px;display:flex;gap:4px}
.slider-arrows span{width:26px;height:34px;background:#0f2540;display:block}
.monitor{left:622px;top:205px;width:490px;height:410px;background:linear-gradient(#eaeef3,#b9c3cf);border-radius:8px}

/* Welcome */
.welcome{top:710px;height:312px;text-align:center}
.welcome h2{margin-top:42px;font-family:'Oswald',sans-serif;font-weight:400;font-size:25px;color:var(--brand-blue)}
.welcome h3{margin-top:10px;font-weight:400;font-size:19px;color:#444}
.welcome p{width:1060px;margin:22px auto 0;font-size:12px;line-height:20px;color:var(--muted)}
.welcome p+p{margin-top:16px}

/* Benefits band */
.benefits{top:1022px;height:430px;background:linear-gradient(#3b3f45,#1e2228 70%,#2b2a26)}
.section-title{font-family:'Oswald',sans-serif;font-weight:400;text-transform:uppercase;text-align:center}
.benefits .section-title{margin-top:54px;color:var(--white);font-size:25px}
.benefit-row{position:absolute;top:140px;left:120px;width:960px;display:flex;justify-content:space-between}
.benefit{width:230px;text-align:center;color:var(--white)}
.ring{width:104px;height:104px;border-radius:50%;background:var(--icon-blue);border:5px solid var(--white);margin:0 auto;display:flex;align-items:center;justify-content:center}
.benefit h4{margin-top:22px;font-size:13px;font-weight:500;text-transform:uppercase}
.benefit p{font-size:10px;line-height:14px;color:#ccc;margin-top:8px}

/* Features with phone */
.features{top:1452px;height:545px;background:linear-gradient(160deg,#f2f2f2,#e2e2e2)}
.feature{position:absolute;width:380px;display:flex;gap:18px}
.feature .circle{flex:0 0 88px;height:88px;border-radius:50%;border:2px solid var(--green);background:var(--white);display:flex;align-items:center;justify-content:center}
.feature h4{font-size:17px;font-weight:500;color:#222;margin-top:10px}
.feature p{font-size:10px;line-height:15px;color:var(--muted);margin-top:6px}
.phone{left:496px;top:75px;width:206px;height:420px;background:linear-gradient(#2d2d2d,#111);border-radius:26px}

/* Testimonial */
.testimonial{top:1997px;height:281px;background:linear-gradient(135deg,#3ea64c,var(--green-dark));text-align:center;color:var(--white)}
.avatar{left:553px;top:38px;width:96px;height:96px;border-radius:50%;border:4px solid var(--white);background:linear-gradient(#c9a07f,#7a5540)}
.t-arrow{top:74px;font-size:28px}
.testimonial blockquote{position:absolute;top:155px;left:150px;width:900px;font-size:13px;line-height:22px;font-style:italic}
.testimonial cite{position:absolute;top:212px;left:0;width:1200px;font-size:13px}

/* Services */
.services{top:2278px;height:767px;background:var(--pale-blue);text-align:center}
.services .section-title{margin-top:45px;font-size:25px;color:#222}
.services .sub{font-size:17px;color:#555;margin-top:10px}
.service-grid{position:absolute;left:60px;top:152px;width:1080px;display:grid;grid-template-columns:repeat(3,360px);row-gap:44px}
.service .ring{width:104px;height:104px;border:none;background:var(--icon-blue)}
.service h4{margin-top:26px;font-size:13px;font-weight:500;text-transform:uppercase;color:#222}
.service p{margin:10px auto 0;width:270px;font-size:11px;line-height:16px;color:var(--muted)}
.services .cta{position:absolute;top:668px;left:0;width:1200px;display:flex;justify-content:center;gap:22px}
.services .cta .btn{width:178px;padding:13px 0;font-size:17px}

/* Trust strip */
.trust{top:3045px;height:158px;background:var(--white)}
.trust h3{position:absolute;left:90px;top:46px;font-family:'Ubuntu',sans-serif;font-weight:500;font-size:24px;color:var(--brand-blue)}
.trust p{position:absolute;left:90px;top:88px;font-size:18px;color:#333}
.badge{position:absolute;border-radius:6px}

/* Footer */
.footer{top:3203px;height:152px;background:var(--footer-blue);color:var(--white)}
.footer h5{font-size:13px;font-weight:500;margin-bottom:8px}
.col{position:absolute;top:22px;font-size:10px;line-height:14px}
.col ul{list-style:none}
.col li::before{content:"› "}
.field{display:flex;margin-top:10px}
.field span{background:var(--white);color:#999;width:140px;padding:6px 10px;border-radius:3px 0 0 3px}
.field b{background:var(--black);padding:6px 12px;font-weight:400}
.socials{display:flex;gap:10px;margin-top:10px}
.socials i{width:24px;height:24px;border:1px solid var(--white);border-radius:50%;display:block}
.bottom-bar{top:3355px;height:140px;background:var(--black);color:#ccc}
.bottom-bar .mini{left:130px;top:16px;font-size:12px;color:#ccc;text-align:center}
.bottom-bar .mini i{display:block;width:22px;height:22px;border:1px solid #999;border-radius:50%;margin:0 auto 4px}
.bottom-bar .copy{right:88px;top:30px;font-size:11px}
</style>
</head>
<body>

<header class="hero">
  <div class="abs brand"><span class="brand-mark"></span>Brivel Marketing</div>
  <nav class="abs nav">
    <span class="active">Home</span><span>Features</span><span>Pricing</span><span>Contact</span><span>Skipper</span><span>Log In</span><span>Preview Your App</span>
  </nav>
  <span class="abs btn-login">LOGIN</span>
  <div class="abs hero-title">
    <h1>WELCOME TO THE REVOLUTION</h1>
    <h2>Mobile Apps &amp; Mobile Websites made easy!</h2>
    <p>BRIVELAPP.COM was built with small businesses in mind. Our goal is to help small businesses grow through affordable mobile marketing!</p>
  </div>
  <a class="btn btn-green">Sample of our Apps</a>
  <div class="abs slider-arrows"><span></span><span></span></div>
  <div class="abs monitor" role="img" aria-label="Desktop monitor displaying the Brivel Tech brand"></div>
</header>

<section class="welcome">
  <h2>WELCOME TO OUR BRIVEL INC</h2>
  <h3>We provide the easiest way for businesses to create Mobile Apps!</h3>
  <p>Consumers use their mobile devices to find the information they want, as soon as they want it. They depend on the instant accessibility of mobile apps to quickly tell them what they need to know, so they can make their purchasing decisions and get on with what they're doing.</p>
  <p>Smart business owners understand the power and importance of mobile marketing to their bottom line. They use mobile apps to connect with customers, share relevant news, offer great deals, increase foot traffic, take reservations, and boost their revenues. Whether they deliver a service, sell products in a store, or run a successful restaurant, they know that having a mobile app is one of the most effective ways to reach their customers, whether they're on the go or standing still.</p>
</section>

<section class="benefits" role="img" aria-label="Dark city skyline at dusk behind the benefits">
  <h2 class="section-title">Having a beautiful customized app allows businesses to</h2>
  <div class="benefit-row">
    <div class="benefit"><div class="ring"><svg width="40" height="32" viewBox="0 0 40 32" fill="#fff"><circle cx="20" cy="9" r="7"/><circle cx="7" cy="12" r="5"/><circle cx="33" cy="12" r="5"/><path d="M8 32c0-8 5-13 12-13s12 5 12 13z"/></svg></div><h4>Build customer loyalty</h4><p>Make your customers feel special by offering discounts, coupons, and promotions just for using your app</p></div>
    <div class="benefit"><div class="ring"><svg width="40" height="34" viewBox="0 0 40 34" fill="none" stroke="#fff" stroke-width="3"><rect x="2" y="2" width="36" height="24" rx="2"/><path d="M14 32h12M20 26v6"/></svg></div><h4>Send push notifications</h4><p>Deliver instant messages to your customers' mobile phones whenever you wish. Only a few emails get opened.</p></div>
    <div class="benefit"><div class="ring"><svg width="38" height="34" viewBox="0 0 38 34" fill="#fff"><path d="M2 16L36 2 28 32 18 22 12 30 12 20 30 6 10 18z"/></svg></div><h4>Create viral buzz</h4><p>Let customers quickly tell all of their friends about you using the built-in sharing capabilities of social networks.</p></div>
    <div class="benefit"><div class="ring"><svg width="30" height="38" viewBox="0 0 30 38" fill="#fff"><path d="M2 2h18l8 8v26H2z"/><path d="M8 18h14M8 24h14M8 30h10" stroke="#2a8be0" stroke-width="2"/></svg></div><h4>Grow your list</h4><p>Gather names and email addresses directly inside your app and easily export them into your favorite email marketing</p></div>
  </div>
</section>

<section class="features">
  <div class="feature" style="left:90px;top:40px"><div class="circle"><svg width="34" height="34" viewBox="0 0 34 34" fill="none" stroke="#3aa04a" stroke-width="3"><rect x="3" y="6" width="28" height="25"/><path d="M3 13h28M10 2v8M24 2v8"/></svg></div><div><h4>Promote special events</h4><p>Provide up-to-date information about all of your business events, sales, and promotions with an in-app events calendar that anyone can access.</p></div></div>
  <div class="feature" style="left:90px;top:170px"><div class="circle"><svg width="34" height="30" viewBox="0 0 38 34" fill="#3aa04a"><path d="M2 16L36 2 28 32 18 22 12 30 12 20 30 6 10 18z"/></svg></div><div><h4>Gain more credibility.</h4><p>These are still the early years of the mobile app. Having one adds serious credibility to your business—especially among those who don't</p></div></div>
  <div class="feature" style="left:90px;top:300px"><div class="circle"><svg width="36" height="30" viewBox="0 0 40 32" fill="#3aa04a"><circle cx="20" cy="9" r="7"/><circle cx="7" cy="12" r="5"/><circle cx="33" cy="12" r="5"/><path d="M8 32c0-8 5-13 12-13s12 5 12 13z"/></svg></div><div><h4>Keep customers informed</h4><p>Fill your app with information about your business, service offerings, product samples, menus, and more. There's a tab for just about</p></div></div>
  <div class="abs phone" role="img" aria-label="Smartphone displaying the Brivel Marketing brand"></div>
  <div class="feature" style="left:756px;top:40px"><div class="circle"><svg width="34" height="28" viewBox="0 0 34 28" fill="none" stroke="#3aa04a" stroke-width="3"><path d="M4 8h26M24 2l6 6-6 6M30 20H4M10 14l-6 6 6 6"/></svg></div><div><h4>Connect with ease</h4><p>Make it simple for customers to reach you using one-touch calling, email, a website link, and GPS directions to your business—all from inside</p></div></div>
  <div class="feature" style="left:756px;top:170px"><div class="circle"><svg width="26" height="34" viewBox="0 0 30 38" fill="#3aa04a"><path d="M2 2h18l8 8v26H2z"/><path d="M8 18h14M8 24h14M8 30h10" stroke="#fff" stroke-width="2"/></svg></div><div><h4>Get instant feedback.</h4><p>Allow customers to leave feedback on your fan wall, share photos, make restaurant reservations, and send comments in a variety of ways.</p></div></div>
  <div class="feature" style="left:756px;top:300px"><div class="circle"><svg width="32" height="32" viewBox="0 0 32 32" fill="#3aa04a"><rect x="2" y="14" width="7" height="16"/><path d="M11 14l7-12c3 0 4 2 3 6l-1 4h9c2 0 3 2 2 4l-3 12c-1 2-2 2-4 2H11z"/></svg></div><div><h4>Track your success</h4><p>Use robust analytics to track daily, weekly, and monthly downloads of your app.</p></div></div>
</section>

<section class="testimonial">
  <span class="abs t-arrow" style="left:512px">‹</span>
  <div class="abs avatar" role="img" aria-label="Customer portrait"></div>
  <span class="abs t-arrow" style="left:670px">›</span>
  <blockquote>“ Lorem Ipsum has been the industry's standard dummy text ever since the 1500s, when an unknown printer took a galley of type and scrambled it to make a type specimen book. It has survived not only five centuries, but also the leap into electronic typesetting, remaining essentially ”</blockquote>
  <cite>Neque porro quisquam est</cite>
</section>

<section class="services">
  <h2 class="section-title">The #1 mobile app &amp; mobile website creator for small businesses</h2>
  <p class="sub">Neque porro quisquam est qui dolorem ipsum quia dolor sit amet</p>
  <div class="service-grid">
    <div class="service"><div class="ring"><svg width="40" height="28" viewBox="0 0 40 28" fill="none" stroke="#fff" stroke-width="3"><rect x="6" y="2" width="28" height="18"/><path d="M1 25h38"/></svg></div><h4>Preview online</h4><p>We allow you to preview your apps as we build it</p></div>
    <div class="service"><div class="ring"><svg width="40" height="34" viewBox="0 0 40 34" fill="#fff"><rect x="12" y="2" width="16" height="14" rx="2"/><rect x="2" y="18" width="16" height="14" rx="2"/><rect x="22" y="18" width="16" height="14" rx="2"/></svg></div><h4>Incredibly easy</h4><p>Our easy to use content manage system allows for beautiful app designs.</p></div>
    <div class="service"><div class="ring"><svg width="30" height="36" viewBox="0 0 30 36" fill="#fff"><ellipse cx="15" cy="6" rx="13" ry="5"/><path d="M2 10c0 6 26 6 26 0v7c0 6-26 6-26 0zM2 21c0 6 26 6 26 0v8c0 6-26 6-26 0z"/></svg></div><h4>Powerful hosting</h4><p>Our servers are hosted in the cloud using the latest hosting technology with 99.9% uptime for your apps.</p></div>
    <div class="service"><div class="ring"><svg width="22" height="36" viewBox="0 0 22 36" fill="none" stroke="#fff" stroke-width="3"><rect x="2" y="2" width="18" height="32" rx="3"/><path d="M9 29h4"/></svg></div><h4>Apps &amp; websites</h4><p>We build and create native apps for phones, tablets, &amp; every major platform, and mobile websites.</p></div>
    <div class="service"><div class="ring"><svg width="36" height="32" viewBox="0 0 38 34" fill="#fff"><path d="M2 16L36 2 28 32 18 22 12 30 12 20 30 6 10 18z"/></svg></div><h4>Customize everything</h4><p>Customize every pixel inside your mobile apps within minutes using our pre-built designs or create your own.</p></div>
    <div class="service"><div class="ring"><svg width="28" height="36" viewBox="0 0 30 38" fill="#fff"><path d="M2 2h18l8 8v26H2z"/><path d="M8 18h14M8 24h14M8 30h10" stroke="#2a8be0" stroke-width="2"/></svg></div><h4>Extremely affordable</h4><p>Is more affordable than a newspaper ad and shows a huge return on investment for businesses.</p></div>
  </div>
  <div class="cta"><a class="btn btn-blue">Learn More</a><a class="btn btn-green">Log In Here</a></div>
</section>

<section class="trust">
  <h3>Small Businesses Trust BRIVEL INC. Worldwide</h3>
  <p>BRIVEL INC. is making mobile apps affordable and simple for small businesses.</p>
  <div class="badge" style="left:912px;top:58px;width:48px;height:54px;background:#e0552a"></div>
  <div class="badge" style="left:976px;top:36px;width:44px;height:80px;background:#2b2b2b;border-radius:8px"></div>
  <div class="badge" style="left:1034px;top:62px;width:42px;height:50px;background:#8fc23c"></div>
</section>

<footer class="footer">
  <div class="col" style="left:90px;width:250px">
    <h5 style="margin-bottom:2px">BRIVEL INC.</h5>
    <div style="font-size:9px;margin-bottom:6px">A Delaware Corporation</div>
    <div>Lorem Ipsum has been the industry's standard dummy text ever since the 1500s, when an unknown printer took a galley of type and scrambled it to make a type specimen book.</div>
  </div>
  <div class="col" style="left:430px"><h5>LINKS</h5><ul><li>Customer Support</li><li>Documentation</li><li>Resources</li><li>General FAQs</li><li>Shortcodes</li></ul></div>
  <div class="col" style="left:626px"><h5>GET IN TOUCH</h5><div>Address : 1420 Harbor View Rd,<br>Fairmont, NJ</div><div style="margin-top:8px">Phone : 555.010.2847</div><div style="margin-top:8px">Email : info@samplemail.com</div></div>
  <div class="col" style="left:908px;width:210px"><h5>NEWSLETTER</h5><div>Your about us information would fit here nicely.</div><div class="field"><span>Email address</span><b>Submit</b></div><div class="socials" style="margin-left:44px"><i></i><i></i><i></i></div></div>
</footer>

<footer class="bottom-bar">
  <div class="abs mini"><i></i>Brivel Tech</div>
  <div class="abs copy">Copyright © 2016. All Rights Reserved</div>
</footer>

</body>
</html>
```